BrookvaleTech Website Design

To design a website for BrookvaleTech, a software development company. The website should reflect the branding of our company, which is Smart, Beautiful, and Sophisticated. The existing website is www.brookvaletech.com.sg

```html
<!DOCTYPE html>
<html lang="en">
<head>
<meta charset="utf-8">
<title>BrookvaleTech</title>
<link href="https://fonts.googleapis.com/css2?family=Open+Sans:wght@400;600;700&display=swap" rel="stylesheet">
<style>
:root{
  --navy:#0c3350;
  --navy-dark:#082a44;
  --accent:#c8492a;
  --grey:#d5d8da;
  --text:#222;
  --white:#fff;
  --dot:#3a3a3a;
}
*{margin:0;padding:0;box-sizing:border-box}
html,body{width:1166px;height:1200px;overflow:hidden;background:var(--white)}
body{position:relative;font-family:"Open Sans",sans-serif;color:var(--text)}
.abs{position:absolute}
.brand{left:45px;top:34px;display:flex;align-items:center;gap:12px}
.brand-mark{width:62px;height:62px;border-radius:50%;background:var(--navy)}
.brand-name{font-size:32px;font-weight:400;color:#1d7fc4}
.main-nav{left:0;top:119px;width:1166px;height:57px;background:var(--navy);box-shadow:0 3px 4px rgba(0,0,0,.3)}
.main-nav a{position:absolute;top:13px;color:var(--white);font-size:23px;text-decoration:none}
.hero-title{left:87px;top:226px;font-size:41px;color:var(--navy);font-weight:400}
.hero-text{left:88px;top:306px;font-size:22px;line-height:31px;color:#333}
.hero-device{left:575px;top:213px;width:466px;height:306px;border-radius:20px;border:3px solid #bbb;
  background:radial-gradient(ellipse at 55% 50%,#5fc3f0 0%,#1a78c8 40%,#111 75%)}
.slider-dots{left:444px;top:537px;width:180px;height:26px}
.features{left:0;top:589px;width:1166px;height:461px;background:var(--grey)}
.feature{position:absolute}
.feature-icon{position:absolute;left:0;top:0;width:40px;height:40px}
.feature-title{position:absolute;left:60px;top:4px;font-size:23px;color:var(--accent);white-space:nowrap}
.feature-body{position:absolute;left:3px;top:50px;font-size:14.5px;line-height:18.6px;white-space:nowrap;color:#222}
.btn-more{position:absolute;width:117px;height:33px;border-radius:4px;background:var(--navy);color:var(--white);
  font-size:18px;font-weight:700;text-align:center;line-height:33px}
.site-footer{left:0;top:1050px;width:1166px;height:150px;background:var(--navy-dark);color:var(--white)}
.foot-col{position:absolute;top:12px}
.foot-head{font-size:13.5px;font-weight:700;padding-bottom:1px;border-bottom:2px dotted var(--white);display:inline-block}
.foot-text{font-size:10.5px;line-height:14.4px;margin-top:8px}
.social{display:flex;align-items:center;gap:10px;height:29px;font-size:11px;font-weight:700}
.social-mark{width:22px;height:22px;border-radius:3px;background:#5a88c0}
.news{font-size:11px;font-weight:700;line-height:14.4px;margin-top:12px}
.copyright{right:47px;top:12px;font-size:13.5px;font-weight:700}
</style>
</head>
<body>
<header>
  <div class="abs brand"><span class="brand-mark"></span><span class="brand-name">BrookvaleTech</span></div>
  <nav class="abs main-nav">
    <a style="left:87px" href="#">Home</a>
    <a style="left:231px" href="#">About Us</a>
    <a style="left:403px" href="#">Products &amp; Services</a>
    <a style="left:685px" href="#">The Team</a>
    <a style="left:872px" href="#">Contact Us</a>
  </nav>
</header>

<section>
  <h1 class="abs hero-title">LOREM IPSUM</h1>
  <p class="abs hero-text">Lorem ipsum dolor sit amet, consectetuer<br>adipiscing elit<br>sed diam nonummy nibh euismod tincidunt</p>
  <div class="abs hero-device" role="img" aria-label="Tablet computer showing a blue desktop screen"></div>
  <svg class="abs slider-dots" viewBox="0 0 180 26">
    <g fill="var(--dot)">
      <circle cx="13" cy="12" r="12"/><circle cx="49" cy="12" r="12"/><circle cx="87" cy="12" r="12"/><circle cx="124" cy="12" r="12"/>
    </g>
    <circle cx="162" cy="12" r="12" fill="var(--navy)"/>
  </svg>
</section>

<svg width="0" height="0" style="position:absolute">
  <symbol id="team-icon" viewBox="0 0 40 40">
    <circle cx="20" cy="20" r="20" fill="var(--accent)"/>
    <g fill="var(--white)">
      <circle cx="13" cy="14" r="3.5"/><circle cx="27" cy="14" r="3.5"/><circle cx="20" cy="12" r="4"/>
      <path d="M7 26c0-5 3-7 6-7s4 1 4 1v6z"/><path d="M33 26c0-5-3-7-6-7s-4 1-4 1v6z"/>
      <path d="M13 28c0-6 3-9 7-9s7 3 7 9z"/>
    </g>
  </symbol>
</svg>

<section class="abs features">
  <div class="feature" style="left:91px;top:23px">
    <svg class="feature-icon"><use href="#team-icon"/></svg>
    <h2 class="feature-title" style="font-weight:400">OUR STORY</h2>
    <p class="feature-body">Lorem ipsum dolor sit amet, consectetuer adipiscing elit<br>sed diam nonummy nibh euismod tincidunt ut laoreet<br>dolore magna aliquam erat volutpat. Ut wisi enim ad<br>minim veniam, quis nostrud exerci tation ullamcorper<br>suscipit lobortis nisl ut aliquip ex ea commodo consequat.</p>
  </div>
  <div class="btn-more" style="left:338px;top:179px">More</div>

  <div class="feature" style="left:637px;top:23px">
    <svg class="feature-icon"><use href="#team-icon"/></svg>
    <h2 class="feature-title" style="left:58px;font-weight:400">BOARD OF DIRECTORS</h2>
    <p class="feature-body" style="left:11px">Dr Adrian Hale (Founder and CEO) adrian@brookvalegroup.com.sg<br>Mr Colin Reyes PBM<br>Ms Nora Whitfield<br>Mr Darren Cole<br>Ms Elise Hart</p>
  </div>
  <div class="btn-more" style="left:1003px;top:179px">More</div>

  <div class="feature" style="left:88px;top:239px">
    <svg class="feature-icon"><use href="#team-icon"/></svg>
    <h2 class="feature-title" style="left:63px;font-weight:400">GIVING BACK TO SOCIETY</h2>
    <p class="feature-body" style="left:7px">We believe in giving back to community and society.<br>We develop software and applications that benefit human<br>kinds and society for free for non-profit organization.</p>
  </div>
  <div class="btn-more" style="left:342px;top:378px">More</div>

  <div class="feature" style="left:637px;top:239px">
    <svg class="feature-icon"><use href="#team-icon"/></svg>
    <h2 class="feature-title" style="left:58px;font-weight:400">WE ARE HIRING</h2>
    <p class="feature-body" style="left:3px">We are looking for talented individuals who are passionate in technology<br>and wanting to have a rewarding and fulfilling career.<br>SOFTWARE ENGINEER: design, architect, develop software, quality assurance<br>and lead application development.</p>
  </div>
  <div class="btn-more" style="left:1002px;top:378px">More</div>
</section>

<footer class="abs site-footer">
  <div class="foot-col" style="left:85px">
    <span class="foot-head">BrookvaleTech Pte Ltd</span>
    <p class="foot-text">No.8 Harbour Lane, #03-17<br>Harbourside Centre<br>Singapore 048620<br>(DID): (65) 6400 1201<br>Tel: (65) 6400 1202<br>Fax: (65) 6400 1203<br>hello@brookvalegroup.com.sg</p>
  </div>
  <div class="foot-col" style="left:345px">
    <span class="foot-head">Follow us&nbsp;&nbsp;&nbsp;&nbsp;&nbsp;&nbsp;&nbsp;&nbsp;&nbsp;&nbsp;&nbsp;&nbsp;&nbsp;&nbsp;&nbsp;&nbsp;&nbsp;&nbsp;</span>
    <div style="margin-top:8px">
      <div class="social"><span class="social-mark"></span>BrookvaleTech Pte Ltd</div>
      <div class="social"><span class="social-mark"></span>@BrookvaleTech Pte Ltd</div>
      <div class="social"><span class="social-mark" style="background:#8a7a68"></span>BrookvaleTech Pte Ltd</div>
    </div>
  </div>
  <div class="foot-col" style="left:573px">
    <span class="foot-head">News&nbsp;&nbsp;&nbsp;&nbsp;&nbsp;&nbsp;&nbsp;&nbsp;&nbsp;&nbsp;&nbsp;&nbsp;&nbsp;&nbsp;&nbsp;&nbsp;&nbsp;&nbsp;&nbsp;&nbsp;&nbsp;&nbsp;&nbsp;&nbsp;&nbsp;&nbsp;&nbsp;</span>
    <p class="news">News 1<br>News 2<br>News 3<br>News 4<br>News 5</p>
  </div>
  <p class="abs copyright">Copyright&nbsp; BrookvaleTech Pte Ltd 2014</p>
</footer>
</body>
</html>
```